Certified Notary Signing Agent Business Card Design

I need a modern, visually appealing two-sided business card for my mobile notary signing agent business which clearly communicates my certification by the Federal Sealwork Guild ("FSG") and Deed Closing Method ("DCM"). It should be clean and easy to read and trust focused. While I am not committed to specific fonts and colors, I do like the colors in both my final logo and a sample logo (color examples only). I want to hand out a business card that is easy to locate in a stack and differentiates itself easily from others as it is an extremely crowded market space.

Target Market(s)

Title Companies, Escrow Officers, Real Estate Agents, Real Estate Lenders

Industry/Entity Type

Real Estate Lending

Contact Information for Business Card

I need a two-sided business card for my mobile notary signing agent business that prominently displays my photo, logo (potentially, just on the back), my service areas, phone, email, url and an FSG certification and DCM certification. On the back side of the card I would like my url, logo and potentially certification icons. On the back, I MAY want to add language that I have been an FSG Certified NSA for 10 + years and have performed over 8k in real estate loan transactions. I have attached a very old biz card circa 2007 that I designed myself on a card ordering platform. While it's not great, it can display how I crammed all of the data on a single card. I am NOT suggesting replicating this design in any form but provide it as reference material only,

Font styles to use
Sans Serif

Requirements
Must have
• Name: Marla Vostrick, Certified Notary Signing Agent Phone: 936.555.0142 URL: www.PrimeQuillSigners.com Email: marla@primequillsigners.com, Counties serviced: Montgomery, Grimes, N. Harris, Walker, Waller, Federal Sealwork Guild Badge, Deed Closing Method Badge (still need to upload this)
Nice to have
• I am open to color variations on my logo as illustrated in the attachment labeled as Logo Sample Colors Only (11A) that has a slate blue/grey background w/white lettering and gold pen and circles

```html
<!DOCTYPE html>
<html lang="en">
<head>
<meta charset="utf-8">
<title>Marla Vostrick – Business Card</title>
<link href="https://fonts.googleapis.com/css2?family=Arimo:wght@400;700&display=swap" rel="stylesheet">
<style>
  :root {
    --backdrop: #9a9a9a;
    --slate: #353e4b;
    --gold: #b9a87b;
    --white: #f1f1f1;
    --badge-light: #e4e7ee;
    --badge-muted: #5a6474;
  }
  * { margin: 0; padding: 0; box-sizing: border-box; }
  html, body {
    width: 1200px; height: 903px; overflow: hidden;
    background: var(--backdrop);
    font-family: "Arimo", Arial, sans-serif;
  }
  .canvas { position: relative; width: 1200px; height: 903px; }
  .card {
    position: absolute; top: 169px;
    width: 353px; height: 618px;
    background: var(--slate);
  }
  .card--front { left: 195px; }
  .card--back { left: 635px; }

  .portrait {
    position: absolute; left: 89px; top: 58px;
    width: 166px; height: 166px; border-radius: 50%;
    border: 4px solid var(--gold);
    padding: 6px;
  }
  .portrait__photo {
    width: 100%; height: 100%; border-radius: 50%;
    background: radial-gradient(circle at 55% 45%, #e6b9a5 0%, #c99a83 45%, #8b6d57 80%, #4e4a4a 100%);
  }
  .agent-name {
    position: absolute; top: 267px; width: 100%; text-align: center;
    color: var(--gold); font-weight: 700; font-size: 23px; letter-spacing: 0.3px;
  }
  .agent-title {
    position: absolute; top: 296px; width: 100%; text-align: center;
    color: var(--white); font-size: 14.5px;
  }
  .contact-icons {
    position: absolute; top: 333px; width: 100%;
    display: flex; justify-content: center; gap: 14px;
  }
  .contact-icons svg { width: 16px; height: 16px; }
  .contact-list {
    position: absolute; top: 375px; width: 100%; text-align: center;
    color: var(--white); font-size: 14.5px; line-height: 18.5px; list-style: none;
  }
  .service-area {
    position: absolute; top: 444px; left: 20px; right: 20px; text-align: center;
    color: var(--gold); font-size: 11px; line-height: 14px;
  }
  .badge-row {
    position: absolute; top: 488px; left: 0; width: 100%;
    display: flex; justify-content: center; align-items: center; gap: 18px;
  }
  .cert-badge {
    width: 86px; height: 86px; border-radius: 50%;
    background: var(--badge-light);
  }
  .method-badge {
    width: 76px; height: 76px; border-radius: 8px;
    background: var(--badge-muted);
  }
  .brand-seal {
    width: 90px; height: 90px; border-radius: 50%;
    border: 2px solid var(--gold);
    display: flex; align-items: center; justify-content: center; text-align: center;
    color: var(--white); font-weight: 700; font-size: 12px; line-height: 14px;
  }
  .brand-mark {
    position: absolute; left: 83px; top: 206px;
    width: 186px; height: 186px; border-radius: 50%;
    border: 3px solid var(--gold);
    display: flex; align-items: center; justify-content: center; text-align: center;
    color: var(--white); font-weight: 700; font-size: 22px; line-height: 27px; letter-spacing: 0.5px;
  }
  .back-url {
    position: absolute; top: 420px; width: 100%; text-align: center;
    color: var(--gold); font-size: 14.5px;
  }
</style>
</head>
<body>
<main class="canvas">
  <section class="card card--front">
    <div class="portrait">
      <div class="portrait__photo" role="img" aria-label="Portrait photo of Marla Vostrick"></div>
    </div>
    <h1 class="agent-name">MARLA VOSTRICK</h1>
    <p class="agent-title">Certified Notary Signing Agent</p>
    <div class="contact-icons" aria-hidden="true">
      <svg viewBox="0 0 24 24"><path fill="var(--gold)" d="M6.6 2.5l3 3.6-2 2.2c1.3 2.9 3.4 5 6.2 6.3l2.1-2 3.7 3-1.9 3.4C10.5 19 5 13.5 3.1 4.4z"/></svg>
      <svg viewBox="0 0 24 24"><rect x="2" y="5" width="20" height="14" fill="var(--gold)"/><path d="M2.5 5.5L12 13l9.5-7.5" fill="none" stroke="var(--slate)" stroke-width="1.6"/></svg>
      <svg viewBox="0 0 24 24"><circle cx="12" cy="12" r="10" fill="var(--gold)"/><path d="M8 5c2 2 0 4 2 5s1 4 3 5M15 4c-1 2 1 3 3 3M16 14c1 2 0 4-1 5" fill="none" stroke="var(--slate)" stroke-width="1.6"/></svg>
    </div>
    <ul class="contact-list">
      <li>936.555.0142</li>
      <li>marla@primequillsigners.com</li>
      <li>www.PrimeQuillSigners.com</li>
    </ul>
    <p class="service-area">Serving Montgomery, Grimes, N. Harris, Walker &amp; Waller Counties</p>
    <div class="badge-row">
      <div class="cert-badge" role="img" aria-label="Federal Sealwork Guild certification badge"></div>
      <div class="method-badge" role="img" aria-label="Deed Closing Method certification badge"></div>
      <div class="brand-seal">Prime<br>Quill<br>Signers</div>
    </div>
  </section>

  <section class="card card--back">
    <div class="brand-mark">Prime Quill<br>Signers</div>
    <p class="back-url">www.PrimeQuillSigners.com</p>
  </section>
</main>
</body>
</html>
```